Healthcare Technology Company Business Card Design

Hi,

We require a new business card design thats catchy and professional.
Our target audience is healthcare professionals. See supplied artwork for our logo.

If you think its achievable please try add the tag line, not necessary however.
"Developing technologies to improve patient care and release operation benefits"

We'll require the following information on the card. No need to have the subject titles but i've referenced them for your convenience.

Personal Details
Paul Dwyer
Position: Director
Phone Number - 03 9472 5836
Mobile Number - 0438 275 904
Email: firstname.lastname@mediqbay.com.au

Company Details
Suite 31, 286 Keldon Street
Port Melbourne, Victoria
Fax: 03 8241 3975
mediqbay.com.au

Prefer a thinner design than the normal stock standard business card dimensions.
Please ensure there is adequate bleed.

Target Market(s)

Healthcare Professionals

Industry/Entity Type

Healthcare

Font styles to use
Sans Serif

Requirements
Must have
• Clean, Sharp Looks
Should not have
• Any healthcare symbols

```html
<!DOCTYPE html>
<html lang="en">
<head>
<meta charset="utf-8">
<title>Mediqbay Business Card</title>
<link rel="stylesheet" href="https://fonts.googleapis.com/css2?family=PT+Sans+Narrow:wght@400;700&display=swap">
<style>
  :root {
    --backdrop: #274c61;
    --card-blue: #386a90;
    --card-blue-light: #3f7298;
    --brand-blue: #35678f;
    --brand-orange: #ef8f2e;
    --paper: #ffffff;
    --ink: #2a2a2a;
    --rule: rgba(255, 255, 255, 0.35);
  }
  * { margin: 0; padding: 0; box-sizing: border-box; }
  html, body {
    width: 1200px;
    height: 910px;
    overflow: hidden;
    background: var(--backdrop);
    font-family: "PT Sans Narrow", "Arial Narrow", sans-serif;
  }
  .stage { position: relative; width: 1200px; height: 910px; }

  .card {
    position: absolute;
    width: 500px;
    height: 255px;
    box-shadow: 10px 12px 18px rgba(10, 30, 42, 0.55);
  }

  /* Front side */
  .card-front {
    left: 91px;
    top: 83px;
    background: linear-gradient(135deg, var(--card-blue) 0%, var(--card-blue-light) 100%);
    border: 1px solid rgba(255, 255, 255, 0.25);
  }
  .card-front .brand {
    position: absolute;
    left: 0; right: 0;
    top: 78px;
    display: flex;
    align-items: center;
    justify-content: center;
    gap: 16px;
    color: var(--paper);
  }
  .card-front .brand-dot {
    width: 30px; height: 30px;
    border-radius: 50%;
    background: var(--paper);
  }
  .card-front .brand-name {
    font-weight: 700;
    font-size: 66px;
    line-height: 1;
    letter-spacing: -0.5px;
  }
  .card-front .tagline-rule {
    position: absolute;
    left: 13px; right: 13px;
    top: 228px;
    height: 1px;
    background: var(--rule);
  }
  .card-front .tagline {
    position: absolute;
    left: 0; right: 0;
    top: 235px;
    text-align: center;
    color: var(--paper);
    font-size: 15px;
    letter-spacing: 0.4px;
  }

  /* Back side */
  .card-back {
    left: 389px;
    top: 432px;
    background: var(--paper);
  }
  .card-back .brand {
    position: absolute;
    left: 23px;
    top: 28px;
    display: flex;
    align-items: center;
    gap: 10px;
  }
  .card-back .brand-dot {
    width: 22px; height: 22px;
    border-radius: 50%;
    background: var(--brand-orange);
  }
  .card-back .brand-name {
    font-weight: 700;
    font-size: 42px;
    line-height: 1;
    color: var(--brand-blue);
  }
  .contact {
    position: absolute;
    right: 28px;
    top: 70px;
    text-align: right;
    color: var(--ink);
    font-size: 15px;
    line-height: 19px;
  }
  .person {
    display: inline-block;
    text-align: left;
    margin-bottom: 4px;
    margin-right: 16px;
  }
  .person-name, .person-role {
    border-left: 4px solid var(--brand-blue);
    padding-left: 10px;
    line-height: 19px;
  }
  .person-name { font-weight: 700; }
  .person-role { border-left-color: var(--brand-orange); font-style: italic; font-family: "PT Sans Narrow", sans-serif; }
  .company {
    position: absolute;
    left: 0; right: 0;
    top: 205px;
    text-align: center;
    color: var(--ink);
    font-size: 15px;
    line-height: 19px;
    letter-spacing: 0.2px;
  }
</style>
</head>
<body>
<main class="stage">
  <section class="card card-front" aria-label="Card front">
    <div class="brand">
      <span class="brand-dot"></span>
      <span class="brand-name">Mediqbay</span>
    </div>
    <div class="tagline-rule"></div>
    <p class="tagline">Developing technologies to improve patient care and release operation benefits</p>
  </section>

  <section class="card card-back" aria-label="Card back">
    <div class="brand">
      <span class="brand-dot"></span>
      <span class="brand-name">Mediqbay</span>
    </div>
    <div class="contact">
      <div class="person">
        <div class="person-name">Paul Dwyer</div>
        <div class="person-role">Director</div>
      </div>
      <div class="phone">Phone - 03 9472 5836</div>
      <div class="mobile">Mobile - 0438 275 904</div>
    </div>
    <div class="company">
      <p>Suite 31, 286 Keldon Street&nbsp; Port Melbourne, Victoria . Fax: 03 8241 3975</p>
      <p>Web : mediqbay.com.au, Email: firstname.lastname@mediqbay.com.au</p>
    </div>
  </section>
</main>
</body>
</html>
```